Exclusive Furniture Company
Relunda GmbH
Project: Exclusive Furniture Company
Exclusive Furniture Company - General Merchandise
Creative Brief
Professional
Tarin HOLDEVA
CEO
Wolkenriedstrasse 4 8124 Lindwiler - Zürich Switzerland
t.tarin@relunda.ch
www.relunda.ch
Only the symbol R from Logo
Sarah2014 Sarah2014
Dear Designers I need Business Card and Stationary! (not only Business Cards) Thanks in advance Greta
Dear Designer, Please try the black color in other color variants... Thanks in advance! Greta
Dear Designer, Back of the business card is OK Fron part only with logo! see atachemnt: http://relunda.ch/logo/business-card-relunda.png Thanks in advance! Greta PS: I apologize for my English mistakes.

```html
<!DOCTYPE html>
<html lang="en">
<head>
<meta charset="utf-8">
<title>Relunda GmbH – Business Card</title>
<link rel="stylesheet" href="https://fonts.googleapis.com/css2?family=Open+Sans:wght@400;600;700;800&display=swap">
<style>
  :root {
    --backdrop: #d9d9db;
    --card: #ffffff;
    --brand-red: #c8102e;
    --ink: #3b3b3d;
    --title-pink: #d9345a;
    --rule-grey: #c9c9cc;
    --on-red: #ffffff;
  }
  * { margin: 0; padding: 0; box-sizing: border-box; }
  html, body {
    width: 1200px; height: 902px; overflow: hidden;
    background: var(--backdrop);
    font-family: "Open Sans", Arial, sans-serif;
  }
  .stage { position: relative; width: 1200px; height: 902px; }
  .card {
    position: absolute; width: 600px; height: 343px;
    background: var(--card);
    box-shadow: 0 10px 24px rgba(0,0,0,0.18);
    overflow: hidden;
  }
  .card--front { left: 80px; top: 90px; }
  .card--back { left: 520px; top: 470px; }

  .wordmark { display: flex; align-items: center; }
  .wordmark__square { background: var(--brand-red); flex: none; }
  .wordmark__name { color: var(--ink); font-weight: 800; letter-spacing: 0.04em; }

  .card--front .wordmark {
    position: absolute; inset: 0;
    justify-content: center; gap: 16px;
  }
  .card--front .wordmark__square { width: 46px; height: 46px; }
  .card--front .wordmark__name { font-size: 50px; }

  .card--back .wordmark { position: absolute; left: 36px; top: 66px; gap: 10px; }
  .card--back .wordmark__square { width: 30px; height: 30px; }
  .card--back .wordmark__name { font-size: 30px; }

  .contact-panel {
    position: absolute; top: 0; right: 0; bottom: 0; width: 230px;
    background: var(--brand-red);
  }
  .panel-rule {
    position: absolute; top: 0; bottom: 0; right: 242px; width: 4px;
    background: var(--rule-grey);
  }

  .holder { position: absolute; left: 38px; top: 222px; }
  .holder__name { color: var(--brand-red); font-weight: 700; font-size: 17px; }
  .holder__title { color: var(--title-pink); font-size: 14px; margin-top: 2px; }

  .contact {
    position: absolute; right: 22px; top: 32px;
    list-style: none; text-align: right;
    color: var(--on-red); font-size: 12px; line-height: 20px;
  }
  .contact li { display: flex; justify-content: flex-end; align-items: center; gap: 6px; }
  .contact svg { width: 11px; height: 11px; fill: var(--on-red); flex: none; }
  .contact .no-icon { padding-right: 17px; }
</style>
</head>
<body>
<main class="stage">
  <section class="card card--front" aria-label="Card front">
    <div class="wordmark">
      <span class="wordmark__square"></span>
      <span class="wordmark__name">RELUNDA</span>
    </div>
  </section>

  <section class="card card--back" aria-label="Card back">
    <div class="panel-rule"></div>
    <div class="contact-panel"></div>

    <div class="wordmark">
      <span class="wordmark__square"></span>
      <span class="wordmark__name">RELUNDA</span>
    </div>

    <div class="holder">
      <p class="holder__name">Liora Venncroft</p>
      <p class="holder__title">Consultant</p>
    </div>

    <ul class="contact">
      <li>Wolkenriedstrasse 4
        <svg viewBox="0 0 12 12"><path d="M6 0a4 4 0 0 0-4 4c0 3 4 8 4 8s4-5 4-8a4 4 0 0 0-4-4zm0 5.5A1.5 1.5 0 1 1 6 2.5a1.5 1.5 0 0 1 0 3z"/></svg></li>
      <li class="no-icon">8124 Lindwiler</li>
      <li>044 210 5837
        <svg viewBox="0 0 12 12"><path d="M2.5 0.5l2 2.5-1.2 1.5a7 7 0 0 0 4.2 4.2L9 7.5l2.5 2-1.5 2C5 11.5 0.5 7 0.5 2z"/></svg></li>
      <li>044 210 5838
        <svg viewBox="0 0 12 12"><rect x="1" y="3" width="10" height="7" rx="1"/><rect x="3" y="1" width="6" height="3"/></svg></li>
      <li>t.tarin@relunda.ch
        <svg viewBox="0 0 12 12"><path d="M0.5 2.5h11v7h-11z M0.5 2.5l5.5 4 5.5-4" fill="none" stroke="#fff" stroke-width="1"/></svg></li>
      <li class="no-icon">www.relunda.ch</li>
    </ul>
  </section>
</main>
</body>
</html>
```